QORVIX needs a new business card!

QORVIX is a group of gaming enthusiasts who are looking for a new corporate business card.

The typeface should be modern and minimalist with attention paid to spacing between the letters and the letters 'qorvix' look relative to each other.

Should clean, crisp and minimalist - looking serious overall but with slight tweaks to the letters to make them look playful...

Black on white is fine.

Details on the card should include:
-the word 'qorvix'
-a job title (use any, for e.g. founder)
-a name (e.g. Ned Pallister)
-phone number
-email address

For inspiration: http://brevant.tamblework-cdn.example/wp-content/uploads/2013/07/kelo-1.jpg

Target Market(s)

Video gaming enthusiasts

Industry/Entity Type

Business

Requirements
Must have
• Black letter on white background.
The word "qorvix"
Nice to have
• Maybe use a conservative font like Gibraltar or Helvetica and tweaking each letter individually.

You can insert normal job titles under the "qorvix" typeface
Should not have
• Should not be cartoony or childish fonts. No colors.

```html
<!DOCTYPE html>
<html lang="en">
<head>
<meta charset="utf-8">
<title>QORVIX — Business Card</title>
<link rel="stylesheet" href="https://fonts.googleapis.com/css2?family=Lato:wght@700;900&display=swap">
<style>
  :root {
    --card-bg: #ffffff;
    --ink: #000000;
    --ink-muted: #a8a8a8;
  }
  html, body {
    margin: 0;
    padding: 0;
    overflow: hidden;
    background: var(--card-bg);
  }
  .card {
    position: relative;
    width: 1200px;
    height: 667px;
    background: var(--card-bg);
    overflow: hidden;
  }
  .wordmark {
    position: absolute;
    left: 0;
    top: 0;
    width: 1200px;
    height: 667px;
  }
  .wordmark text {
    font-family: "Lato", Arial, sans-serif;
    font-weight: 900;
    font-size: 232px;
    letter-spacing: -0.045em;
    fill: var(--ink);
  }
  .contact-line {
    position: absolute;
    right: 53px;
    top: 574px;
    margin: 0;
    font-family: "Lato", Arial, sans-serif;
    font-weight: 700;
    font-size: 17px;
    letter-spacing: 0.01em;
    text-transform: uppercase;
    color: var(--ink-muted);
    white-space: nowrap;
  }
  .contact-line .person-name {
    color: var(--ink);
  }
  .contact-line .sep {
    margin: 0 0.3em;
  }
</style>
</head>
<body>
  <main class="card">
    <svg class="wordmark" viewBox="0 0 1200 667" aria-label="qorvix">
      <text x="66" y="391">qorvix</text>
    </svg>
    <p class="contact-line">
      <span class="person-name">Ned Pallister</span><span class="sep">·</span><span class="job-title">Founder</span><span class="sep">·</span><span class="phone">+00 000 0000</span><span class="sep">·</span><span class="email">mail@qorvix.com</span>
    </p>
  </main>
</body>
</html>
```